Business Card Design

Need business card design for all carpentry & construction solutions. We would like to see designs that use black as a background with orange writing as it would stand out.

Business

KRV CONTRACTING
MARTIN COLBY
14 PELLINGTON ST
BRENNOCK VALE
QT 6721
0498371265
krvcontracting@tramlex.com

```html
<!DOCTYPE html>
<html lang="en">
<head>
<meta charset="UTF-8">
<title>KRV Contracting – Business Card</title>
<link href="https://fonts.googleapis.com/css2?family=Montserrat:wght@300;400;600&display=swap" rel="stylesheet">
<style>
  :root {
    --stage: #ecebe8;
    --card: #fbfbfb;
    --band-grey: #e4e4e4;
    --charcoal: #3d3d3d;
    --orange: #e05014;
    --ink: #3a3a3a;
    --white: #ffffff;
  }
  * { box-sizing: border-box; margin: 0; padding: 0; }
  html, body {
    width: 1200px; height: 800px; overflow: hidden;
    background: var(--stage);
    font-family: "Montserrat", Arial, sans-serif;
  }
  .sheet {
    width: 1200px; height: 800px;
    display: flex; align-items: center; justify-content: center; gap: 40px;
  }
  .card {
    position: relative;
    width: 540px; height: 300px;
    background: var(--card);
    box-shadow: 0 6px 18px rgba(0,0,0,0.12);
    overflow: hidden;
  }

  /* Back: contact side */
  .card-back .brand-panel {
    position: absolute; left: 0; top: 46px;
    width: 250px; height: 216px;
    background: var(--charcoal);
    border-top-right-radius: 10px;
    display: flex; align-items: center; justify-content: center; gap: 10px;
  }
  .card-back .contact-band {
    position: absolute; left: 250px; right: 0; top: 28px; height: 150px;
    background: linear-gradient(90deg, var(--card) 0%, var(--band-grey) 100%);
  }
  .contact-list {
    position: absolute; left: 272px; top: 46px;
    list-style: none; color: var(--ink);
    font-size: 12.5px; font-weight: 400; letter-spacing: 0.3px; line-height: 1.45;
  }
  .contact-list li { display: flex; gap: 10px; align-items: flex-start; margin-bottom: 3px; }
  .contact-list svg { width: 12px; height: 12px; flex: none; margin-top: 3px; fill: var(--ink); }
  .contact-list .email { font-size: 12px; }

  /* Front: name side */
  .card-front .name-band {
    position: absolute; left: 0; top: 112px;
    width: 282px; height: 84px;
    background: var(--orange);
    display: flex; align-items: center; padding-left: 26px;
  }
  .card-front .person-name {
    color: var(--white); font-weight: 600; font-size: 22px; letter-spacing: 0.2px;
  }
  .card-front .brand-band {
    position: absolute; left: 298px; right: 0; top: 118px; height: 80px;
    background: var(--charcoal);
    display: flex; align-items: center; justify-content: center; gap: 10px;
  }

  .brand-mark { width: 14px; height: 14px; background: var(--orange); flex: none; }
  .brand-name {
    color: var(--orange); font-weight: 600; font-size: 15px; letter-spacing: 0.5px;
    white-space: nowrap;
  }
</style>
</head>
<body>
<main class="sheet">

  <section class="card card-back" aria-label="Card back">
    <div class="brand-panel">
      <span class="brand-mark"></span>
      <span class="brand-name">KRV CONTRACTING</span>
    </div>
    <div class="contact-band"></div>
    <ul class="contact-list">
      <li>
        <svg viewBox="0 0 12 12"><path d="M6 0a4 4 0 0 0-4 4c0 3 4 8 4 8s4-5 4-8a4 4 0 0 0-4-4zm0 5.6A1.6 1.6 0 1 1 6 2.4a1.6 1.6 0 0 1 0 3.2z"/></svg>
        <span>14 PELLINGTON ST<br>BRENNOCK VALE<br>QT 6721</span>
      </li>
      <li>
        <svg viewBox="0 0 12 12"><path d="M3 0.5l2 2.5-1.2 1.4c.6 1.4 1.6 2.4 3 3L8 6.2l2.5 2-1 2.6C5 11 1 7 1.2 2.5z"/></svg>
        <span>0498371265</span>
      </li>
      <li class="email">
        <svg viewBox="0 0 12 12"><path d="M1 2.5h10v7H1zm1 1v.3l4 2.7 4-2.7v-.3zm0 1.5v3.5h8V5L6 7.6z"/></svg>
        <span>krvcontracting@tramlex.com</span>
      </li>
    </ul>
  </section>

  <section class="card card-front" aria-label="Card front">
    <div class="name-band">
      <span class="person-name">MARTIN COLBY</span>
    </div>
    <div class="brand-band">
      <span class="brand-mark"></span>
      <span class="brand-name">KRV CONTRACTING</span>
    </div>
  </section>

</main>
</body>
</html>
```